RWT Installations Ltd Business Cards

We need a business card with our business logo. We provide window and door installations on high-rises in west coast British Colombia, Canada.

I would like my business information and details on one side of the card, and the other side the company name with logo

Target Market(s)

General Contractors

Industry/Entity Type

Construction

Contact Information for Business Card

one side i want my company name and logo in the dark theme logo that i provided

Requirements
Must have
• Tomas Verelund, 15559284016, RWTInstallations@mailvera.example, 1408-5192 Pellow Avenue Burnaby BC, V0X 1Z9, Owner & Manager

```html
<!DOCTYPE html>
<html lang="en">
<head>
<meta charset="utf-8">
<title>RWT Installations Ltd — Business Cards</title>
<link href="https://fonts.googleapis.com/css2?family=Exo+2:wght@500;600&family=Open+Sans:wght@400&display=swap" rel="stylesheet">
<style>
  :root {
    --stage: #6e6e6e;
    --stage-dark: #4a4a4a;
    --card: #232323;
    --card-edge: #1a1a1a;
    --brand-blue: #3fb2ee;
    --text-grey: #b9b9b9;
    --text-soft: #9a9a9a;
    --deco-light: #4a4a4a;
    --deco-dark: #1c1c1c;
  }
  * { margin: 0; padding: 0; box-sizing: border-box; }
  html, body { width: 1200px; height: 876px; overflow: hidden; }
  body {
    background: radial-gradient(ellipse at 55% 40%, var(--stage) 0%, var(--stage-dark) 100%);
    position: relative;
    font-family: "Open Sans", Arial, sans-serif;
  }
  .card {
    position: absolute;
    top: 289px;
    width: 520px;
    height: 298px;
    border-radius: 3px;
    background: var(--card);
    box-shadow: 0 1px 0 var(--card-edge), 0 3px 0 var(--card-edge), 0 5px 0 var(--card-edge), 0 18px 30px rgba(0,0,0,.45);
    overflow: hidden;
  }
  .card-front { left: 60px; }
  .card-back { left: 620px; }

  .brand {
    display: flex;
    align-items: center;
    gap: 10px;
    font-family: "Exo 2", sans-serif;
    font-weight: 600;
    color: var(--brand-blue);
    letter-spacing: .04em;
    text-transform: uppercase;
  }
  .brand-mark {
    width: 14px; height: 14px;
    background: var(--brand-blue);
  }
  .card-front .brand { position: absolute; left: 34px; top: 32px; font-size: 21px; }

  .contact-list {
    position: absolute;
    left: 34px; top: 84px;
    list-style: none;
    font-size: 12.5px;
    line-height: 21px;
    color: var(--text-grey);
  }
  .contact-list li { display: flex; align-items: center; gap: 8px; }
  .contact-list .no-icon { padding-left: 20px; }
  .contact-list svg { width: 12px; height: 12px; fill: var(--brand-blue); flex: none; }

  .person {
    position: absolute;
    right: 34px; top: 100px;
    text-align: right;
  }
  .person-name {
    font-family: "Exo 2", sans-serif;
    font-weight: 500;
    font-size: 20px;
    letter-spacing: .1em;
    color: var(--brand-blue);
    text-transform: uppercase;
  }
  .person-title { font-size: 13px; color: var(--text-soft); margin-top: 2px; }

  .front-graphic {
    position: absolute;
    left: 230px; top: 182px;
    width: 290px; height: 116px;
    background: linear-gradient(120deg, var(--deco-dark) 0%, var(--deco-light) 60%, #2a2a2a 100%);
  }

  .back-scene {
    position: absolute; inset: 0;
    background: linear-gradient(135deg, #2a2826 0%, #3a3734 45%, #24221f 100%);
  }
  .card-back .brand {
    position: absolute; inset: 0;
    justify-content: center;
    font-size: 26px;
  }
</style>
</head>
<body>
  <section class="card card-front" aria-label="Business card front">
    <div class="brand"><span class="brand-mark"></span>RWT Installations Ltd</div>
    <ul class="contact-list">
      <li class="no-icon">1408-5192 Pellow Avenue</li>
      <li class="no-icon">Burnaby BC, V0X 1Z9</li>
      <li><svg viewBox="0 0 24 24" aria-hidden="true"><path d="M6.6 10.8c1.4 2.8 3.8 5.1 6.6 6.6l2.2-2.2c.3-.3.7-.4 1-.2 1.1.4 2.3.6 3.6.6.6 0 1 .4 1 1V20c0 .6-.4 1-1 1C10.6 21 3 13.4 3 4c0-.6.4-1 1-1h3.5c.6 0 1 .4 1 1 0 1.3.2 2.5.6 3.6.1.3 0 .7-.2 1z"/></svg>(555) 928-4016</li>
      <li><svg viewBox="0 0 24 24" aria-hidden="true"><path d="M2 5h20v14H2zm2 2v.5l8 5 8-5V7zm0 2.9V17h16V9.9l-8 5z"/></svg>RWTInstallations@mailvera.example</li>
      <li><svg viewBox="0 0 24 24" aria-hidden="true"><path d="M12 2a10 10 0 100 20 10 10 0 000-20zm6.9 9h-3a15 15 0 00-1.4-6 8 8 0 014.4 6zM12 4c.9 1.2 1.7 3.7 1.9 7h-3.8c.2-3.3 1-5.8 1.9-7zM9.5 5a15 15 0 00-1.4 6h-3a8 8 0 014.4-6zM5.1 13h3a15 15 0 001.4 6 8 8 0 01-4.4-6zM12 20c-.9-1.2-1.7-3.7-1.9-7h3.8c-.2 3.3-1 5.8-1.9 7zm2.5-1a15 15 0 001.4-6h3a8 8 0 01-4.4 6z"/></svg>rwtinstallations.example</li>
    </ul>
    <div class="person">
      <p class="person-name">Tomas Verelund</p>
      <p class="person-title">Owner &amp; Manager</p>
    </div>
    <div class="front-graphic" role="img" aria-label="Large dark grey decorative graphic filling the lower part of the card"></div>
  </section>

  <section class="card card-back" aria-label="Business card back">
    <div class="back-scene" role="img" aria-label="Dim photograph of an office interior with a plant, in dark brown tones"></div>
    <div class="brand"><span class="brand-mark"></span>RWT Installations Ltd</div>
  </section>
</body>
</html>
```